Heron Renovation Group Postcard Design Project

I'm a General Contractor specializing in luxury residential remodeling.

THIS IS AN EDDM POSTCARD. THE ENTIRE BACK SIDE OF THE CARD WILL BE USED.

I FORGOT TO MENTION THIS IN MY ORIGINAL BRIEF.

Target Market(s)

OLD, rich people so please make sure the fonts are clear and crisp.

Font styles to use
Sans Serif

```html
<!DOCTYPE html>
<html lang="en">
<head>
<meta charset="utf-8">
<title>Heron Renovation Group – EDDM Postcard</title>
<link rel="stylesheet" href="https://fonts.googleapis.com/css2?family=Raleway:wght@200;300;400;600;700;800&display=swap">
<style>
  :root {
    --red: #d42027;
    --red-dark: #a5161c;
    --ink: #2b2b2b;
    --grey: #555a60;
    --paper: #ffffff;
    --blueprint-light: #eef2f7;
    --blueprint-mid: #d6dfea;
    --photo-sky: #2f4f86;
    --photo-warm: #c9a46a;
    --backdrop: #ececec;
  }
  * { box-sizing: border-box; margin: 0; padding: 0; }
  html, body {
    width: 1200px; height: 558px; overflow: hidden;
    background: var(--backdrop);
    font-family: "Raleway", Arial, sans-serif;
  }
  .sheet {
    position: relative; width: 1200px; height: 558px;
    display: flex; gap: 20px; padding: 79px 20px;
  }
  .postcard {
    position: relative; width: 570px; height: 400px;
    background: var(--paper); overflow: hidden;
    box-shadow: 0 4px 14px rgba(0,0,0,.18);
  }
  .blueprint-bg {
    position: absolute; inset: 0;
    background: linear-gradient(135deg, var(--blueprint-light) 0%, #fff 45%, var(--blueprint-mid) 100%);
  }

  /* ---------- Front ---------- */
  .service-band {
    position: absolute; left: 0; right: 0; top: 212px; height: 72px;
    background: linear-gradient(90deg, var(--red-dark), var(--red));
  }
  .photo-cluster { position: absolute; left: 0; top: 0; width: 570px; height: 400px; }
  .headline { position: absolute; left: 26px; top: 30px; line-height: 1; }
  .headline .bold-line { font-weight: 800; color: var(--red); text-transform: uppercase; }
  .headline .thin-line { font-weight: 200; color: var(--ink); text-transform: uppercase; }
  .headline .l1 { font-size: 38px; letter-spacing: .5px; }
  .headline .l2 { font-size: 60px; letter-spacing: 1px; margin-top: 2px; }
  .headline .l3 { font-size: 26px; margin-top: 6px; }
  .headline .l4 { font-size: 20px; margin-top: 4px; letter-spacing: .5px; }
  .services {
    position: absolute; left: 26px; top: 222px;
    list-style: none; color: #fff; font-weight: 600; font-size: 15.5px; line-height: 17px;
  }
  .contact, .back-contact { position: absolute; left: 26px; line-height: 1; }
  .contact { top: 292px; }
  .back-contact { top: 292px; }
  .contact .name, .back-contact .name { font-size: 15px; font-weight: 300; color: var(--ink); text-transform: uppercase; }
  .contact .phone, .back-contact .phone { font-size: 42px; font-weight: 800; color: var(--red); margin-top: 3px; }
  .contact .web, .back-contact .web { font-size: 16px; font-weight: 600; color: var(--grey); margin-top: 2px; }
  .credentials {
    position: absolute; left: 0; right: 0; bottom: 0; height: 26px;
    background: var(--red); color: #fff;
    font-size: 12px; font-weight: 600; letter-spacing: 3px;
    display: flex; align-items: center; padding-left: 26px;
  }

  /* ---------- Back ---------- */
  .stamp-box {
    position: absolute; right: 34px; top: 24px; width: 62px; height: 72px;
    border: 1.5px solid var(--ink); background: #fff;
  }
  .company-name {
    position: absolute; left: 300px; top: 110px;
    font-size: 17px; font-weight: 800; color: var(--red); text-transform: uppercase;
  }
  .address-lines { position: absolute; left: 300px; top: 130px; width: 240px; }
  .address-lines span { display: block; height: 28px; border-bottom: 1.5px solid var(--ink); }
  .tagline {
    position: absolute; left: 26px; top: 262px;
    font-size: 15px; font-weight: 700; color: var(--ink);
  }
</style>
</head>
<body>
<main class="sheet">

  <section class="postcard postcard-front">
    <div class="blueprint-bg" role="img" aria-label="Faint blueprint floor plan with a measuring tape"></div>
    <div class="service-band"></div>

    <svg class="photo-cluster" viewBox="0 0 570 400">
      <defs>
        <linearGradient id="photoPool" x1="0" y1="0" x2="0" y2="1">
          <stop offset="0" stop-color="var(--photo-sky)"/>
          <stop offset=".55" stop-color="var(--photo-warm)"/>
          <stop offset="1" stop-color="#1d3f6b"/>
        </linearGradient>
        <linearGradient id="photoDusk" x1="0" y1="0" x2="0" y2="1">
          <stop offset="0" stop-color="#3d5f9c"/>
          <stop offset=".6" stop-color="#8a7a64"/>
          <stop offset="1" stop-color="#2a6b93"/>
        </linearGradient>
        <linearGradient id="photoPlan" x1="0" y1="0" x2="1" y2="1">
          <stop offset="0" stop-color="#f4f7fb"/>
          <stop offset="1" stop-color="#b9c9dc"/>
        </linearGradient>
      </defs>
      <circle cx="520" cy="22" r="82" fill="var(--red)"/>
      <circle cx="520" cy="22" r="72" fill="url(#photoPlan)" role="img" aria-label="Close-up of architectural plans"/>
      <circle cx="445" cy="168" r="122" fill="var(--red)"/>
      <circle cx="445" cy="168" r="110" fill="url(#photoDusk)" role="img" aria-label="Photo of a luxury home with lit windows reflected in a pool at dusk"/>
      <circle cx="365" cy="96" r="80" fill="var(--red)"/>
      <circle cx="365" cy="96" r="70" fill="url(#photoPool)" role="img" aria-label="Photo of a stone-clad home with an evening pool"/>
      <circle cx="398" cy="22" r="40" fill="#fff" stroke="var(--red)" stroke-width="6"/>
      <text x="398" y="18" text-anchor="middle" font-family="Raleway, sans-serif" font-weight="800" font-size="14" fill="var(--red)">SINCE</text>
      <text x="398" y="36" text-anchor="middle" font-family="Raleway, sans-serif" font-weight="800" font-size="16" fill="var(--red)">1985</text>
    </svg>

    <h1 class="headline">
      <div class="bold-line l1">Remodeling</div>
      <div class="thin-line l2">Luxury</div>
      <div class="bold-line l3">Homes &amp; Building</div>
      <div class="thin-line l4">Lasting Relationships</div>
    </h1>

    <ul class="services">
      <li>All Phases of Residential Remodeling</li>
      <li>Partial &amp; Large Scale Renovations</li>
      <li>Complimentary Design Services</li>
    </ul>

    <div class="contact">
      <p class="name">Daniel Whitaker, General Contractor</p>
      <p class="phone">480-555-0142</p>
      <p class="web">WWW.HERONRENOVATIONGROUP.COM</p>
    </div>

    <footer class="credentials">Licensed / Bonded / Insured #318406</footer>
  </section>

  <section class="postcard postcard-back">
    <div class="blueprint-bg" role="img" aria-label="Faint blueprint drawing with a pencil across the card"></div>
    <div class="stamp-box"></div>
    <p class="company-name">Heron Renovation Group</p>
    <div class="address-lines"><span></span><span></span><span></span><span></span></div>
    <p class="tagline">Quality Craftsmanship</p>
    <div class="back-contact">
      <p class="name">Daniel Whitaker, General Contractor</p>
      <p class="phone">480-555-0142</p>
      <p class="web">WWW.HERONRENOVATIONGROUP.COM</p>
    </div>
  </section>

</main>
</body>
</html>
```